Re-Design an adult education portal

I need support to re-design an adult education portal. Currently the customer has an incomplete website which should be prepared in a new format.
I have the idea how to realize, but I have no clue how to design it. The hard thing is to have a "beautiful" website with available logo and main color. I hope you can support me.

Name of Website: tovrenu (tovrenu.ch)
Content: adult eduction for adult in safety at work, mountain climbing, dog school. various courses in different areas. But on old webpage is hard to find the different possibilities.
main color: Ral 6011 (green) -> #6C7C59
logo: you see on top of website the logo (2 dogs and a mountain with a colour gradient).

new website: for new webpage I decided to have a navigation for each section of education. In the main area I would like to have some pictures to give an idea what content is behind. At the moment it looks terrible, so I decided to use you as support for me to make the webpage prettier :). And maybe you have an better idea how to make it great. -> current state of new web page: https://tovrenu.bask-om.ch/

Target Market(s)

adult eduction for adult in safety at work, mountain climbing, dog school

Number of Pages Required

1 page

Font styles to use
Serif
Sans Serif

Requirements
Must have
• As main color is set "Ral 6011" (green) -> #6C7C59

```html
<!DOCTYPE html>
<html lang="de">
<head>
<meta charset="utf-8">
<title>tovrenu – Ihr Ausbildungs- und Kurspartner</title>
<link href="https://fonts.googleapis.com/css2?family=Roboto:wght@300;400;500;700&display=swap" rel="stylesheet">
<style>
:root{
  --green:#6C7C59;
  --green-dark:#5d6b4c;
  --ink:#1f1f1f;
  --muted:#444;
  --white:#fff;
  --pill:#c9c9c9;
  --dot-tint:rgba(108,124,89,.10);
}
*{box-sizing:border-box;margin:0;padding:0}
html,body{width:1200px;height:3000px;overflow:hidden;background:#fff}
body{font-family:'Roboto',sans-serif;color:var(--ink)}
.page{position:relative;width:1200px;height:3000px;overflow:hidden}
.abs{position:absolute}
.topbar{left:69px;top:0;width:1061px;height:27px;background:var(--green)}
.brand-box{left:136px;top:0;width:159px;height:84px;background:#fff;box-shadow:0 1px 3px rgba(0,0,0,.15);display:flex;align-items:center;justify-content:center;z-index:3}
.brand-name{font-size:26px;font-weight:400;color:var(--green)}
.nav{left:400px;top:38px;width:710px;display:flex;justify-content:space-between;font-size:15px;font-variant:small-caps;font-weight:500;z-index:3}
.nav span::after{content:"";display:inline-block;width:6px;height:6px;border-right:2px solid var(--ink);border-bottom:2px solid var(--ink);transform:rotate(45deg);margin-left:6px;position:relative;top:-3px}
.hero{left:0;top:66px;width:1200px;height:580px}
.hero-title{left:136px;top:168px;font-size:33px;line-height:38px;color:#fff;font-weight:400}
.hero-text{left:136px;top:273px;font-size:19.5px;line-height:23.5px;color:#fff}
.btn{display:inline-flex;align-items:center;gap:10px;border-radius:20px;font-size:16px;height:38px;padding:0 18px}
.btn::after{content:"";width:6px;height:6px;border-right:2px solid currentColor;border-top:2px solid currentColor;transform:rotate(45deg)}
.btn-light{background:var(--pill);color:#333}
.btn-green{background:var(--green);color:#fff}
.hero-photo{left:658px;top:87px;width:262px;height:461px;background:linear-gradient(180deg,#d9dde6,#aeb8c8);border-radius:40% 40% 6px 6px}
.arrow{font-size:30px;color:#fff;font-weight:700}
.dots{left:598px;top:521px;display:flex;gap:4px}
.dots i{width:12px;height:12px;border:1.5px solid #fff;border-radius:50%}
.dots i:first-child{background:#fff}
.dot-field{background:var(--dot-tint);border-radius:8px}
.section-title{width:1200px;text-align:center;font-size:40px;font-variant:small-caps;font-weight:400}
.divider{height:1px;background:var(--ink)}
.star{font-size:14px;text-align:center;width:20px}
.card{width:278px;background:#fff;border-radius:10px;box-shadow:0 2px 8px rgba(0,0,0,.18);overflow:hidden;text-align:center}
.card .img{width:100%}
.card h3{font-weight:400;font-size:20px;margin-top:14px;line-height:22px}
.card p{font-size:11.5px;line-height:14px;text-align:left;padding:0 20px;margin-top:12px;height:62px}
.card .btn{height:37px;font-size:15.5px;margin-top:16px}
.about-title{left:160px;top:1608px;font-size:42px;font-weight:400}
.about-text{left:160px;top:1692px;width:440px;font-size:16.2px;line-height:20.6px;color:var(--green)}
.ref-sub{width:1200px;text-align:center;font-size:33px;color:var(--green);font-weight:400}
.quote-card{width:391px;height:412px;background:#fff;box-shadow:0 2px 10px rgba(0,0,0,.18)}
.quote-card ul{list-style:none;padding:0 42px;font-size:12px;line-height:26.6px}
.quote-mark{font-size:120px;line-height:1;color:var(--green);font-weight:700;font-family:Georgia,serif}
.avatar{width:82px;height:82px;border-radius:50%}
.person{width:391px;text-align:center}
.person b{display:block;font-weight:400;font-size:20px}
.person span{display:block;font-size:16px;margin-top:6px}
.footer-text{color:var(--ink);font-variant:small-caps}
.foot-h{font-size:25px;font-weight:500;letter-spacing:.5px}
.foot-item{font-size:14.5px;display:flex;align-items:center;gap:22px}
.foot-link{font-size:15px;font-variant:small-caps}
</style>
</head>
<body>
<div class="page">

  <div class="abs topbar"></div>
  <div class="abs brand-box"><span class="brand-name">tovrenu</span></div>
  <nav class="abs nav"><span>Arbeitssicherheit</span><span>CZV</span><span>Erste Hilfe</span><span>Hundeschule</span><span>Bergausbildung</span><span>Tovrenu</span></nav>

  <svg class="abs hero" viewBox="0 0 1200 580" aria-hidden="true">
    <path fill="#6C7C59" d="M69 0H1130V571C1060 585 980 560 900 520C800 470 690 470 600 500C520 528 420 520 320 495C220 470 140 500 69 515Z"/>
  </svg>
  <div class="abs hero-photo" role="img" aria-label="Smiling student carrying a backpack and a stack of books"></div>
  <h1 class="abs hero-title">Ihr Ausbildungs- und<br>Kurspartner</h1>
  <p class="abs hero-text">Wir Bieten Ihren Wünschen Entsprechende<br>Ausbildungen, Zielorientiert Und<br>Ihrem Können Und Wissen Angepasst.</p>
  <a class="abs btn btn-light" style="left:136px;top:370px">Erfahren Sie Mehr</a>
  <div class="abs arrow" style="left:90px;top:302px">«</div>
  <div class="abs arrow" style="left:1086px;top:302px">»</div>
  <div class="abs dots"><i></i><i></i><i></i></div>
  <div class="abs dot-field" style="left:69px;top:515px;width:170px;height:155px" role="img" aria-label="Dotted decoration"></div>

  <h2 class="abs section-title" style="left:0;top:634px">Unsere Dienstleistungen</h2>
  <div class="abs divider" style="left:375px;top:688px;width:212px"></div>
  <div class="abs star" style="left:589px;top:680px">★</div>
  <div class="abs divider" style="left:611px;top:688px;width:212px"></div>
  <div class="abs dot-field" style="left:630px;top:1000px;width:250px;height:250px" role="img" aria-label="Dotted decoration"></div>

  <div class="abs card" style="left:136px;top:732px;height:372px">
    <div class="img" style="height:185px;background:linear-gradient(180deg,#1e2336,#3b3f55)" role="img" aria-label="Rescue team at a night-time car accident"></div>
    <h3>Nothelfer</h3>
    <p>Seit 1990 Sind Wir Im Nothelfer Sektor Haupt Oder Nebenberuflich Tätig. Wir Führen Den \ Nothelferkurs Für Führerscheinerwerbende Von Der VERKA Anerkannt Und Von Der PQS</p>
    <a class="btn btn-green">Weiterlesen</a>
  </div>
  <div class="abs card" style="left:462px;top:732px;height:372px;width:273px">
    <div class="img" style="height:185px;background:linear-gradient(135deg,#9a9a88,#c9c3b0)" role="img" aria-label="Climber on a rock face"></div>
    <h3>Bergausbildung</h3>
    <p>Bei Aktivitäten Am Berg Ist Immer Ein Restrisiko Vorhanden. Durch Mehr Wissen Kann Das Risiko Besser Beurteilt Werden. Mit</p>
    <a class="btn btn-green">Weiterlesen</a>
  </div>
  <div class="abs card" style="left:779px;top:732px;height:372px;width:274px">
    <div class="img" style="height:185px;background:linear-gradient(180deg,#c98a2e,#3a2a18)" role="img" aria-label="Silhouette of a person playing with a dog at sunset"></div>
    <h3>Hundeschule</h3>
    <p>Auf Unserem Hundeplatz Führen Wir Hauptsächlich Welpenkurse, Team-Beurteilungen, Ringtraining Und Abklärungen Durch. Wenn Es Die Lage Erlaubt Sind Wir</p>
    <a class="btn btn-green">Weiterlesen</a>
  </div>

  <div class="abs card" style="left:136px;top:1138px;height:374px">
    <div class="img" style="height:176px;background:linear-gradient(180deg,#6f6a66,#9a938c)" role="img" aria-label="First aid class practising CPR on training dummies"></div>
    <h3>Rettung &amp; Sanität</h3>
    <p>Wir Bieten Ihnen Nach Ihren Wünschen Angepasste Kurse Im Sanitäts Und Rettungsbereich An. Firmenkurse Werden Auf</p>
    <a class="btn btn-green">Weiterlesen</a>
  </div>
  <div class="abs card" style="left:462px;top:1138px;height:374px;width:273px">
    <div class="img" style="height:176px;background:linear-gradient(180deg,#b7cde0,#3e4a5a)" role="img" aria-label="Yellow aerial work platform in front of an industrial building"></div>
    <h3 style="font-size:16.5px;line-height:19px">Hubarbeitsbühnen PSA G A<br>Schulung &amp; Jahreskontrolle</h3>
    <p style="margin-top:10px;height:53px">Wer In Der Schweiz Gefährliche Arbeiten Ausführen Will, Ist Verpflichtet Eine Dementsprechende Schulung Vorgängig Zu</p>
    <a class="btn btn-green">Weiterlesen</a>
  </div>
  <div class="abs card" style="left:779px;top:1138px;height:374px;width:274px">
    <div class="img" style="height:176px;background:linear-gradient(180deg,#c4d3e6,#8b8f96)" role="img" aria-label="Red fire truck in front of snowy mountains"></div>
    <h3 style="margin-top:22px">CZV Kurs</h3>
    <p>Wir Bieten Ihnen Folgende Firmeneigene Kurse An.<br><br>Vorbereitet Für Den Notfall</p>
    <a class="btn btn-green" style="margin-top:10px">Weiterlesen</a>
  </div>

  <h2 class="abs about-title">Über Uns</h2>
  <div class="abs divider" style="left:160px;top:1657px;width:76px"></div>
  <div class="abs star" style="left:236px;top:1649px">★</div>
  <div class="abs divider" style="left:256px;top:1657px;width:66px"></div>
  <p class="abs about-text">In Meiner Beruflichen Laufbahn Erlebte Ich Immer Wieder Situationen, Welche In Mir Die Idee Reifen Liessen, Jedem Interessierten Menschen Ein Grundwissen Zukommen Zu Lassen, Welches Ihn Bei Einer Notsituation Richtig Und Mit Der Nötigen Ruhe Reagieren Lässt Das Zusammenlegen &amp; Kombinieren Von Wissen Und Fertigkeiten Der Verschiedenen Fachbereiche Gibt Dem Menschen Sicherheit Und Vertrauen In Seinem Handeln.</p>
  <a class="abs btn btn-green" style="left:160px;top:1880px;font-size:15.5px">Erfahren Sie Mehr</a>
  <div class="abs dot-field" style="left:866px;top:1600px;width:186px;height:180px" role="img" aria-label="Dotted decoration"></div>
  <div class="abs" style="left:761px;top:1633px;width:255px;height:239px;background:var(--green)"></div>
  <div class="abs" style="left:664px;top:1665px;width:325px;height:226px;background:linear-gradient(180deg,#7e8e6a,#8fae3c)" role="img" aria-label="Couple sitting in a meadow with their three dogs"></div>

  <h2 class="abs section-title" style="left:0;top:1990px;font-variant:normal;font-size:42px">REFERENZEN</h2>
  <div class="abs divider" style="left:488px;top:2046px;width:99px"></div>
  <div class="abs star" style="left:589px;top:2038px">★</div>
  <div class="abs divider" style="left:611px;top:2046px;width:99px"></div>
  <h3 class="abs ref-sub" style="left:0;top:2060px">Was Unsere Kunden Sagen</h3>
  <div class="abs divider" style="left:581px;top:2106px;width:38px"></div>
  <div class="abs dot-field" style="left:134px;top:2115px;width:184px;height:182px" role="img" aria-label="Dotted decoration"></div>
  <div class="abs dot-field" style="left:885px;top:2432px;width:184px;height:180px" role="img" aria-label="Dotted decoration"></div>

  <div class="abs quote-card" style="left:178px;top:2163px">
    <ul style="padding-top:38px">
      <li>Dipl. Fachmann Im Pisten-&amp; Rettungsdienst &amp;</li>
      <li>Ausbildner Talbahnen Verbund</li>
      <li>Lawinenhundeführer &amp; Ausbildner AWRV</li>
      <li>Nothilfeinstruktor (Société Alpine De Certification)</li>
      <li>BLS-AED-Instruktor RRC</li>
      <li>Prüfungsexperte TFH (Teamfähiger Familienhund)</li>
      <li>Prüfungsexperte NHP (Nationaler Hundeführer Pass)</li>
      <li>BLVK Hundetrainer</li>
    </ul>
  </div>
  <div class="abs quote-mark" style="left:216px;top:2128px">“</div>
  <div class="abs avatar" style="left:332px;top:2406px;background:linear-gradient(180deg,#a9b7c9,#3d5166)" role="img" aria-label="Portrait of Lukas Brenner"></div>
  <div class="abs person" style="left:178px;top:2495px"><b>Lukas Brenner</b><span>Schneesportlehrer</span></div>

  <div class="abs quote-card" style="left:629px;top:2163px">
    <ul style="padding-top:49px">
      <li>BLS – AED – Instruktorin RRC</li>
      <li>Nothilfeinstruktorin (Société Alpine De Certification)</li>
      <li>Prüfungsexpertin TFH (Teamfähiger Familienhund)</li>
      <li>Prüfungsexpertin NHP (Nationaler Hundeführer Pass)</li>
      <li>BLVK Hundetrainerin</li>
      <li>Jägerin</li>
    </ul>
  </div>
  <div class="abs quote-mark" style="left:666px;top:2128px">“</div>
  <div class="abs avatar" style="left:784px;top:2406px;background:linear-gradient(180deg,#5b6778,#c2582a)" role="img" aria-label="Portrait of Anna Brenner"></div>
  <div class="abs person" style="left:629px;top:2495px"><b>Anna Brenner</b><span>Fachfrau Gesundheit</span></div>

  <svg class="abs" style="left:0;top:2615px" width="1200" height="385" viewBox="0 0 1200 385" aria-hidden="true">
    <path fill="#6C7C59" d="M69 35C150 5 230 -5 330 10C440 28 520 60 640 80C760 100 820 40 900 50C990 60 1060 100 1130 108V385H69Z"/>
  </svg>
  <div class="abs brand-box" style="left:181px;top:2763px;width:188px;height:100px;box-shadow:none"><span class="brand-name" style="font-size:30px">tovrenu</span></div>
  <div class="abs footer-text" style="left:162px;top:2878px;font-size:34px">Tovrenu GmbH</div>

  <div class="abs foot-h footer-text" style="left:494px;top:2752px;font-variant:normal">CONTACT US</div>
  <div class="abs foot-item footer-text" style="left:494px;top:2813px">
    <svg width="18" height="24" viewBox="0 0 18 24"><path d="M9 0a9 9 0 0 0-9 9c0 7 9 15 9 15s9-8 9-15a9 9 0 0 0-9-9zm0 12.5A3.5 3.5 0 1 1 9 5.5a3.5 3.5 0 0 1 0 7z" fill="#1f1f1f"/></svg>
    <span>Talweg 27, CH-3900 Brig</span></div>
  <div class="abs foot-item footer-text" style="left:494px;top:2857px">
    <svg width="20" height="20" viewBox="0 0 24 24"><path d="M6.6 10.8a15 15 0 0 0 6.6 6.6l2.2-2.2a1 1 0 0 1 1-.25 11.4 11.4 0 0 0 3.6.57 1 1 0 0 1 1 1V20a1 1 0 0 1-1 1A17 17 0 0 1 3 4a1 1 0 0 1 1-1h3.5a1 1 0 0 1 1 1 11.4 11.4 0 0 0 .57 3.6 1 1 0 0 1-.25 1z" fill="#1f1f1f"/></svg>
    <span style="font-variant:normal">+41 79 000 12 34</span></div>
  <div class="abs foot-item footer-text" style="left:494px;top:2902px">
    <svg width="22" height="16" viewBox="0 0 22 16"><rect x="1" y="1" width="20" height="14" fill="#1f1f1f"/><path d="M1 1l10 8 10-8" stroke="#6C7C59" stroke-width="1.6" fill="none"/></svg>
    <span>INFO@TOVRENU.CH</span></div>

  <div class="abs foot-h footer-text" style="left:889px;top:2752px;font-variant:normal">LINKS</div>
  <div class="abs foot-link footer-text" style="left:889px;top:2812px">AGBs</div>
  <div class="abs foot-link footer-text" style="left:889px;top:2847px">Leitbild</div>
  <div class="abs foot-link footer-text" style="left:889px;top:2881px">Zertifikat Qualita</div>
  <div class="abs foot-link footer-text" style="left:889px;top:2916px">Impressum</div>
</div>
</body>
</html>
```